TRPD Marketing Flyers

We would like to make 5 x A4 marketing flyers that we can hand to our customers. We are an engineering company based in Australia.
We make a machine called a Torvane Rotary Pivot Deck (TRPD).
The first flyer we would like to do is give an overview of the TRPD which can be made in 4 different designs.
Then we would like to make a flyer for each design. The 4 different designs are:
Compressor TRPD
Multipurpose TRPD
Rod Storage TRPD
Container TRPD
I have attached images for each desgin as well as the text we require. Our website is www.corvellengineering.com.au for you to look at our colours etc and get a feel for our business. We want the flyer to be modern and clean but classy.
The Corvell Engineering TRPD - this is the text for the overview flyer

```html
<!DOCTYPE html>
<html lang="en">
<head>
<meta charset="utf-8">
<title>Corvell Engineering – TRPD Flyer Set</title>
<link rel="stylesheet" href="https://fonts.googleapis.com/css2?family=Poppins:wght@400;500;600;700;800&display=swap">
<style>
  :root{
    --sheet:#858585;
    --navy:#253f9e;
    --green:#1f9e4b;
    --sky-top:#c4d8f2;
    --sky-bottom:#eef4fc;
    --ink:#33363d;
    --paper:#ffffff;
  }
  *{box-sizing:border-box;margin:0;padding:0}
  html,body{width:918px;height:1200px;overflow:hidden}
  body{background:var(--sheet);font-family:"Poppins",sans-serif;color:var(--ink);position:relative}
  .defs{position:absolute;width:0;height:0}

  .flyer{position:absolute;width:375px;height:529px;background:var(--paper);overflow:hidden}
  .flyer--compressor{left:61px;top:51px}
  .flyer--multipurpose{left:478px;top:51px;width:377px;height:531px}
  .flyer--rod{left:60px;top:614px}
  .flyer--container{left:478px;top:614px}

  .flyer-art{position:absolute;left:0;top:0;width:100%;height:100%}

  .brand{position:absolute;left:18px;top:22px;display:flex;align-items:center;gap:8px}
  .brand-mark{width:18px;height:18px;border-radius:50%;background:var(--navy);flex:none}
  .brand-name{font-weight:600;font-size:14px;line-height:16px;color:var(--navy);letter-spacing:.4px;text-transform:uppercase}

  .flyer-title{position:absolute;right:16px;top:13px;text-align:right;font-weight:800;font-size:19px;line-height:23.5px;color:var(--navy)}
  .flyer-title .accent{color:var(--green)}
  .flyer-rule{position:absolute;right:18px;top:91px;width:108px;height:1px;background:var(--navy)}
  .flyer-rule::after{content:"";position:absolute;right:0;top:-1px;width:22px;height:2px;background:var(--green)}

  .flyer-body{position:absolute;left:29px;font-size:7.9px;line-height:9.6px;color:var(--ink)}
  .flyer-body .lead{color:var(--navy);font-weight:500}
  .flyer-sub{position:absolute;left:29px;font-size:8px;font-weight:600;color:var(--green)}

  .features{position:absolute;list-style:none;font-size:7.5px;line-height:9px;color:var(--ink)}
  .features li{position:relative;padding-left:9px;margin-bottom:4px}
  .features li::before{content:"";position:absolute;left:0;top:1.5px;width:6px;height:6px;border-radius:50%;background:var(--green)}
  .features li::after{content:"";position:absolute;left:1.8px;top:2.6px;width:1.6px;height:2.6px;border:solid #fff;border-width:0 1px 1px 0;transform:rotate(40deg)}

  .flyer-footer{position:absolute;left:0;right:0;top:501px;border-top:1px solid var(--navy);padding:9px 16px 0;display:flex;justify-content:space-between;font-size:7.3px;font-weight:500;color:var(--ink)}
  .flyer-footer span{display:flex;align-items:center;gap:2px}
  .flyer-footer svg{width:7px;height:7px}
</style>
</head>
<body>

<svg class="defs" aria-hidden="true">
  <defs>
    <linearGradient id="sky" x1="0" y1="0" x2="0" y2="1">
      <stop offset="0" stop-color="#c4d8f2"/>
      <stop offset="1" stop-color="#f1f6fd"/>
    </linearGradient>
    <linearGradient id="machineTones" x1="0" y1="0" x2="1" y2="0">
      <stop offset="0" stop-color="#e8edf3"/>
      <stop offset=".35" stop-color="#f0f2f5"/>
      <stop offset=".5" stop-color="#e3c63a"/>
      <stop offset=".78" stop-color="#d7b92e"/>
      <stop offset="1" stop-color="#2a3346"/>
    </linearGradient>
    <linearGradient id="yardTones" x1="0" y1="0" x2="0" y2="1">
      <stop offset="0" stop-color="#b4cbe6"/>
      <stop offset=".3" stop-color="#d9dde2"/>
      <stop offset=".55" stop-color="#eef0f2"/>
      <stop offset=".72" stop-color="#3459b8"/>
      <stop offset=".88" stop-color="#c0594c"/>
      <stop offset="1" stop-color="#9a7d66"/>
    </linearGradient>
    <linearGradient id="fieldTones" x1="0" y1="0" x2="0" y2="1">
      <stop offset="0" stop-color="#dbe4ee"/>
      <stop offset=".3" stop-color="#cfc8c0"/>
      <stop offset=".45" stop-color="#8f5a40"/>
      <stop offset=".6" stop-color="#3a59b0"/>
      <stop offset=".75" stop-color="#b89878"/>
      <stop offset="1" stop-color="#a88a6c"/>
    </linearGradient>
    <linearGradient id="truckTones" x1="0" y1="0" x2="0" y2="1">
      <stop offset="0" stop-color="#c4d6ec"/>
      <stop offset=".25" stop-color="#d9d6cc"/>
      <stop offset=".5" stop-color="#b3b8c0"/>
      <stop offset=".7" stop-color="#2e50a8"/>
      <stop offset=".85" stop-color="#3c3f46"/>
      <stop offset="1" stop-color="#8e9196"/>
    </linearGradient>
    <symbol id="sky-bg" viewBox="0 0 375 529">
      <rect width="375" height="529" fill="#fff"/>
      <rect width="375" height="340" fill="url(#sky)"/>
    </symbol>
    <symbol id="curves" viewBox="0 0 375 529">
      <path d="M0 0 H178 C172 50 128 78 0 80 Z" fill="#fff"/>
      <path d="M0 76 C95 78 160 58 178 14 C168 68 115 96 0 98 Z" fill="var(--navy)"/>
      <path d="M0 256 C120 240 250 250 345 328 C250 268 120 262 0 272 Z" fill="var(--navy)"/>
      <path d="M0 279 C150 262 300 274 375 336 V390 C300 300 150 280 0 284 Z" fill="var(--green)"/>
      <path d="M0 284 C150 280 300 300 375 390 V529 H0 Z" fill="#fff"/>
    </symbol>
    <symbol id="i-phone" viewBox="0 0 10 10"><path d="M2.2 1 L3.8 1 L4.4 3 L3.3 3.8 C3.9 5 5 6.1 6.2 6.7 L7 5.6 L9 6.2 V7.8 C9 8.5 8.4 9 7.7 9 C4 8.7 1.3 6 1 2.3 C1 1.6 1.5 1 2.2 1 Z" fill="none" stroke="var(--green)" stroke-width=".9"/></symbol>
    <symbol id="i-pin" viewBox="0 0 10 10"><path d="M5 9.5 C3 7 1.8 5.3 1.8 3.6 A3.2 3.2 0 0 1 8.2 3.6 C8.2 5.3 7 7 5 9.5 Z" fill="var(--green)"/><circle cx="5" cy="3.6" r="1.2" fill="#fff"/></symbol>
    <symbol id="i-mail" viewBox="0 0 10 10"><rect x=".8" y="2" width="8.4" height="6" fill="none" stroke="var(--green)" stroke-width=".9"/><path d="M.8 2 L5 5.4 L9.2 2" fill="none" stroke="var(--green)" stroke-width=".9"/></symbol>
  </defs>
</svg>

<article class="flyer flyer--compressor">
  <svg class="flyer-art" viewBox="0 0 375 529" preserveAspectRatio="none">
    <use href="#sky-bg"/>
    <path role="img" aria-label="Photo of a yellow drilling compressor mounted on a white Torvane Rotary Pivot Deck with fold-out solar panels" d="M0 196 L90 130 L135 110 L320 108 L338 150 L338 330 L225 344 L95 320 L55 240 L0 245 Z" fill="url(#machineTones)"/>
    <use href="#curves"/>
  </svg>
  <div class="brand"><span class="brand-mark"></span><span class="brand-name">Corvell<br>Engineering</span></div>
  <h1 class="flyer-title">Compressor<br>Torvane Rotary<br><span class="accent">Pivot Deck</span></h1>
  <div class="flyer-rule"></div>
  <p class="flyer-body" style="top:338px;width:285px"><span class="lead">The Compressor Torvane Rotary Pivot Deck</span> is tailored to accommodate compressors used in drilling operations, with jack legs positioned strategically to fit larger compressors between them. Its compact size allows for multiple bases to be transported on a single trailer for convenience during mobilisation.</p>
  <h2 class="flyer-sub" style="top:398px">Highlighted advantages of the Compressor TRPD include:</h2>
  <ul class="features" style="left:29px;top:417px;width:320px">
    <li>Optimal leg spacing for accommodating larger compressors</li>
    <li>Compact design equivalent to a standard 20ft Sea Container, enabling efficient transport of multiple bases on a 40ft trailer.</li>
    <li>Convenient leg placement allowing easy access to all compressor doors for ground-level maintenance.</li>
  </ul>
  <footer class="flyer-footer">
    <span><svg><use href="#i-phone"/></svg>+61 400 555 018</span>
    <span><svg><use href="#i-pin"/></svg>212 Harlow St, Kelmscott 6111</span>
    <span><svg><use href="#i-mail"/></svg>info@corvellengineering.com.au</span>
  </footer>
</article>

<article class="flyer flyer--multipurpose">
  <svg class="flyer-art" viewBox="0 0 375 529" preserveAspectRatio="none">
    <use href="#sky-bg"/>
    <path role="img" aria-label="Photo of a blue Multipurpose Torvane Rotary Pivot Deck carrying a white water tank with tilted solar panels in a yard" d="M0 96 H375 V336 C300 274 150 262 0 279 Z" fill="url(#yardTones)"/>
    <use href="#curves"/>
  </svg>
  <div class="brand"><span class="brand-mark"></span><span class="brand-name">Corvell<br>Engineering</span></div>
  <h1 class="flyer-title">Multipurpose<br>Torvane Rotary<br><span class="accent">Pivot Deck</span></h1>
  <div class="flyer-rule"></div>
  <p class="flyer-body" style="top:352px;width:252px">This <span class="lead">versatile Multipurpose Torvane Rotary Pivot Deck</span> option features a standard flat deck that allows for easy mounting of various equipment configurations to meet the demanding needs of different applications</p>
  <h2 class="flyer-sub" style="top:399px">Our innovative designs include:</h2>
  <ul class="features" style="left:29px;top:418px;width:145px">
    <li>15000L water tank</li>
    <li>12000L water tank</li>
    <li>12000L water tank and 3000L diesel tank with a precision-engineered 24v diesel pump for enhanced fuel delivery</li>
  </ul>
  <ul class="features" style="left:186px;top:421px;width:165px">
    <li>Diamond rod sloop featuring foldable doors at one end and a tilting door at the opposing end, facilitating seamless entry and exit.</li>
    <li>10ft sea container workshop offering a compact yet versatile workspace – air con unit can be added to the workshop.</li>
  </ul>
  <footer class="flyer-footer">
    <span><svg><use href="#i-phone"/></svg>+61 400 555 018</span>
    <span><svg><use href="#i-pin"/></svg>212 Harlow St, Kelmscott 6111</span>
    <span><svg><use href="#i-mail"/></svg>info@corvellengineering.com.au</span>
  </footer>
</article>

<article class="flyer flyer--rod">
  <svg class="flyer-art" viewBox="0 0 375 529" preserveAspectRatio="none">
    <use href="#sky-bg"/>
    <path role="img" aria-label="Photo of a blue pipe storage Torvane Rotary Pivot Deck loaded with rusty drill pipes on a dirt site" d="M0 100 H375 V336 C300 274 150 262 0 279 Z" fill="url(#fieldTones)"/>
    <use href="#curves"/>
  </svg>
  <div class="brand"><span class="brand-mark"></span><span class="brand-name">Corvell<br>Engineering</span></div>
  <h1 class="flyer-title">Pipe Storage<br>Torvane Rotary<br><span class="accent">Pivot Deck</span></h1>
  <div class="flyer-rule"></div>
  <p class="flyer-body" style="top:339px;width:242px"><span class="lead">The Pipe storage Torvane rotary pivot deck</span> is designed where Drill Rods or casing can be stored on the base. This design has tilting legs to allow the pipes to be picked up from the one side, without lifting them over the legs. The features of this design are;</p>
  <h2 class="flyer-sub" style="top:398px">Our innovative designs include:</h2>
  <ul class="features" style="left:29px;top:417px;width:150px">
    <li>The overall length of the base is 6.5m, to allow storage of drill Pipes / casing.</li>
    <li>Fold down headboard on one end to allow for easier loading / unloading.</li>
  </ul>
  <ul class="features" style="left:185px;top:420px;width:150px">
    <li>The legs fold down on one side to allow IT access without lifting the Pipes or casing over the legs.</li>
  </ul>
  <footer class="flyer-footer">
    <span><svg><use href="#i-phone"/></svg>+61 400 555 018</span>
    <span><svg><use href="#i-pin"/></svg>212 Harlow St, Kelmscott 6111</span>
    <span><svg><use href="#i-mail"/></svg>info@corvellengineering.com.au</span>
  </footer>
</article>

<article class="flyer flyer--container">
  <svg class="flyer-art" viewBox="0 0 375 529" preserveAspectRatio="none">
    <use href="#sky-bg"/>
    <path role="img" aria-label="Photo of a truck carrying a Container Torvane Rotary Pivot Deck with a silver 10ft sea container" d="M0 100 H375 V336 C300 274 150 262 0 279 Z" fill="url(#truckTones)"/>
    <use href="#curves"/>
  </svg>
  <div class="brand"><span class="brand-mark"></span><span class="brand-name">Corvell<br>Engineering</span></div>
  <h1 class="flyer-title">Container<br>Torvane Rotary<br><span class="accent">Pivot Deck</span></h1>
  <div class="flyer-rule"></div>
  <p class="flyer-body" style="top:343px;width:278px">The <span class="lead">Container Torvane Rotary Pivot Deck</span> is designed with a longer frame to accommodate a standard 20ft sea container between the legs. With a clearance between the legs of 6.5m, this design also works for rod storage and handling if it is a requirement to manoeuvre the rods between the legs. Some of the setups we have completed with this design are;</p>
  <ul class="features" style="left:29px;top:417px;width:150px">
    <li>Standard 20ft sea container mounted on the base</li>
    <li>Standard 20ft container, split in 2 with one end being a workshop, and one being an air-conditioned office.</li>
  </ul>
  <ul class="features" style="left:185px;top:420px;width:150px">
    <li>Rod handling sloop, operating with a freedom loader, where the rods are passed between the legs.</li>
  </ul>
  <footer class="flyer-footer">
    <span><svg><use href="#i-phone"/></svg>+61 400 555 018</span>
    <span><svg><use href="#i-pin"/></svg>212 Harlow St, Kelmscott 6111</span>
    <span><svg><use href="#i-mail"/></svg>info@corvellengineering.com.au</span>
  </footer>
</article>

</body>
</html>
```